Harvest Cellar

We need desigin for our main page(concept will be used for other pages also).
We already have a logo, and moqup of our main page(see attch).
You could change layers and positions on moqup, but please use logo, and its colors in design creating. (We have logo in different colors, i attached 2 samples, so you could use also another colors if you wish).

Our bussinees will be something similar to BloomLaunch or Seedwell.io, but with some special features. So main idea: start-ups, donations, investemnets

Designs were prefer:
http://seedwell.io/
http://www.bloomlaunch-example.com/

Brief was updated.

Target Market(s)

Clients are middle aged persons, who interested in new start-ups, investments and so on.

Requirements
Must have
• Design must be neat

```html
<!DOCTYPE html>
<html lang="en">
<head>
<meta charset="utf-8">
<title>Harvest Cellar</title>
<link href="https://fonts.googleapis.com/css2?family=Open+Sans:wght@400;600;700&family=Arimo:wght@400;700&display=swap" rel="stylesheet">
<style>
:root{
  --brand:#2b4a85;
  --steel:#5f7598;
  --nav-active:#4a6a9a;
  --ink:#111;
  --col-dark:#2c4676;
  --col-light:#6a84ad;
  --pill:#1f3560;
  --muted:#d3dcec;
  --footer:#dcdcdc;
  --btn:#4a6494;
}
*{box-sizing:border-box;margin:0;padding:0}
html,body{width:1108px;height:1200px;overflow:hidden;background:#fff}
.stage{position:relative;width:1200px;height:1300px;transform:scale(.92333);transform-origin:0 0;font-family:"Open Sans",sans-serif;color:var(--ink);overflow:hidden}
.abs{position:absolute}
.topbar{left:0;top:0;width:1200px;height:6px;background:var(--steel)}
.brand{left:115px;top:14px}
.brand-dot{position:absolute;left:50px;top:0;width:52px;height:52px;border-radius:50%;background:var(--brand)}
.brand-name{position:absolute;left:0;top:66px;white-space:nowrap;font-weight:700;font-size:23px;color:var(--brand);letter-spacing:.3px}
.search{left:914px;top:26px;width:179px;height:30px;background:#e0e0e0;font-size:13px;padding:8px 17px;color:#222}
.nav{top:84px;font-size:12.5px;color:#111;white-space:nowrap}
.nav.active{color:var(--nav-active)}
.hero{left:113px;top:128px;width:980px;height:464px;background:linear-gradient(180deg,#e9eaec 0%,#dcdee2 55%,#f2f3f4 100%)}
.hero-side{left:113px;top:128px;width:317px;height:464px;background:rgba(90,90,90,.9)}
.stats{list-style:none;position:absolute;left:133px;top:188px}
.stats li{height:50px;font-size:18.5px;color:#fff;display:flex;align-items:flex-start;gap:11px;line-height:28px}
.stats svg{margin-top:4px}
.hero-shadow{left:113px;top:592px;width:980px;height:60px;background:radial-gradient(ellipse 55% 100% at 50% 0%,rgba(0,0,0,.45),rgba(0,0,0,0) 100%)}
.dots{left:539px;top:623px;display:flex;gap:3px}
.dots span{width:16px;height:16px;border-radius:50%;background:radial-gradient(circle at 40% 35%,#666,#222)}
.dots span.on{background:radial-gradient(circle at 40% 35%,#ccc,#888)}
.cols{left:113px;top:657px;width:746px;height:362px;display:flex}
.col{flex:1;position:relative;text-align:center;color:#fff}
.col:nth-child(1){background:linear-gradient(90deg,#2a416d,#36507f)}
.col:nth-child(2){background:linear-gradient(90deg,#36507f,#435d8d)}
.col:nth-child(3){background:linear-gradient(90deg,#435d8d,#536e9c)}
.col:nth-child(4){background:linear-gradient(90deg,#536e9c,#6a84ad)}
.col h3{font-weight:400;font-size:16px;margin-top:12px;letter-spacing:.2px}
.thumb{width:133px;height:88px;margin:9px auto 0;background:#fff;padding:6px}
.thumb div{width:100%;height:100%}
.col p{font-family:Arimo,sans-serif;font-size:13px;line-height:15px;color:var(--muted);margin-top:16px}
.bar{width:150px;height:20px;margin:12px auto 0;background:#000;border-radius:10px;position:relative;overflow:hidden}
.bar span{position:absolute;right:0;top:0;width:58px;height:20px;background:#c8c8c8;border-radius:0 10px 10px 0;font-size:8.5px;color:#111;line-height:20px}
.pill{width:140px;height:26px;margin:11px auto 0;background:var(--pill);border-radius:6px;font-family:Arimo,sans-serif;font-size:12.5px;line-height:26px}
.meta{display:flex;justify-content:center;gap:4px;margin-top:15px}
.meta span{background:var(--pill);opacity:.9;height:27px;line-height:27px;font-size:9px;padding:0 6px;white-space:nowrap}
.invest{display:block;width:86px;height:29px;margin:22px auto 0;border:1px solid #c9d4e8;background:#4c6a9c;font-size:13px;line-height:27px}
.tab{top:656px;height:34px;font-size:11.5px;font-weight:600;text-align:center;line-height:38px;border-radius:4px 4px 0 0}
.tab.login{left:931px;width:78px;background:#000;color:#fff}
.tab.signup{left:1014px;width:79px;background:var(--btn);color:#dfe6f2}
.loginbox{left:869px;top:689px;width:224px;height:227px;background:radial-gradient(ellipse at 50% 40%,#2b2b2b,#000 80%);padding:25px 19px;color:#fff;font-size:12.5px}
.loginbox label{display:block}
.loginbox .field{width:186px;height:26px;background:#fff;margin:12px 0 18px}
.forgot{color:#d99cb1;text-decoration:underline;font-size:11px;display:block;margin-top:-1px}
.logbtn{display:block;width:78px;height:28px;margin:14px 0 0 56px;background:var(--btn);border:1px solid #7087b3;text-align:center;line-height:26px;font-size:11.5px}
.video{left:877px;top:939px;width:216px;height:189px;background:#000}
.video .ctl{position:absolute;left:0;bottom:10px;width:216px;height:14px;background:linear-gradient(#777,#333)}
.money{left:0;top:1020px;width:230px;height:280px;background:radial-gradient(ellipse at 40% 60%,rgba(150,175,145,.6),rgba(210,220,205,0) 70%)}
.banner{left:113px;top:1046px;width:745px;height:73px;background:#000;border-radius:6px;color:#fff}
.banner span{position:absolute;left:80px;top:24px;font-size:21px;letter-spacing:.2px}
.yes{position:absolute;left:594px;top:16px;width:106px;height:41px;border-radius:6px;background:linear-gradient(#5c78a8,#3d5787);font-size:19px;text-align:center;line-height:41px}
.social{top:1141px;width:16px;height:16px;background:#111;border-radius:50%}
.footer{left:0;top:1158px;width:1200px;height:142px;background:var(--footer)}
.fcol{position:absolute;top:1166px;width:120px;font-family:Arimo,sans-serif;font-size:8px;line-height:8.5px;color:#111}
.fcol p{margin-bottom:9px}
.flink{top:1285px;font-family:Arimo,sans-serif;font-size:7.5px;font-weight:700;color:#111;white-space:nowrap}
</style>
</head>
<body>
<div class="stage">
  <div class="abs topbar"></div>

  <div class="abs brand">
    <div class="brand-dot"></div>
    <div class="brand-name">HARVEST CELLAR</div>
  </div>

  <div class="abs search">Search ...</div>
  <div class="abs nav active" style="left:613px">HOME</div>
  <div class="abs nav" style="left:701px">HOW IT WORKS</div>
  <div class="abs nav" style="left:845px">PROJECT REVIEW</div>
  <div class="abs nav" style="left:996px">VIRTUAL OFFICE</div>

  <div class="abs hero" role="img" aria-label="Photo of a business team smiling around a meeting table with laptops"></div>
  <div class="abs hero-side"></div>
  <ul class="stats">
    <li><svg width="20" height="18" viewBox="0 0 20 18"><rect x="1" y="4" width="13" height="13" fill="none" stroke="#fff" stroke-width="2"/><path d="M4 10l4 4 11-13" fill="none" stroke="#fff" stroke-width="3"/></svg>$ 50 000 000 of investments</li>
    <li><svg width="20" height="18" viewBox="0 0 20 18"><rect x="1" y="4" width="13" height="13" fill="none" stroke="#fff" stroke-width="2"/><path d="M4 10l4 4 11-13" fill="none" stroke="#fff" stroke-width="3"/></svg>1600 start - ups</li>
    <li><svg width="20" height="18" viewBox="0 0 20 18"><rect x="1" y="4" width="13" height="13" fill="none" stroke="#fff" stroke-width="2"/><path d="M4 10l4 4 11-13" fill="none" stroke="#fff" stroke-width="3"/></svg>700 organizations</li>
    <li><svg width="20" height="18" viewBox="0 0 20 18"><rect x="1" y="4" width="13" height="13" fill="none" stroke="#fff" stroke-width="2"/><path d="M4 10l4 4 11-13" fill="none" stroke="#fff" stroke-width="3"/></svg>10 000 investors</li>
    <li><svg width="20" height="18" viewBox="0 0 20 18"><rect x="1" y="4" width="13" height="13" fill="none" stroke="#fff" stroke-width="2"/><path d="M4 10l4 4 11-13" fill="none" stroke="#fff" stroke-width="3"/></svg>5000 employees</li>
    <li><svg width="20" height="18" viewBox="0 0 20 18"><rect x="1" y="4" width="13" height="13" fill="none" stroke="#fff" stroke-width="2"/><path d="M4 10l4 4 11-13" fill="none" stroke="#fff" stroke-width="3"/></svg>2000 partners</li>
    <li><svg width="20" height="18" viewBox="0 0 20 18"><rect x="1" y="4" width="13" height="13" fill="none" stroke="#fff" stroke-width="2"/><path d="M4 10l4 4 11-13" fill="none" stroke="#fff" stroke-width="3"/></svg>$ 10 000 000 of profits</li>
  </ul>
  <div class="abs hero-shadow"></div>
  <div class="abs dots"><span></span><span></span><span></span><span class="on"></span><span></span></div>

  <div class="abs money" role="img" aria-label="Illustration of scattered banknotes and cash bundles"></div>

  <div class="abs cols">
    <div class="col">
      <h3>RECOMMENDED</h3>
      <div class="thumb"><div role="img" aria-label="Hand placing a coin on a stack with a sprout" style="background:radial-gradient(circle at 55% 65%,#b9b4a4,#f2f2f0 70%)"></div></div>
      <p>Ut wisi enim ad minim<br>veniam, quis nostrud<br>exerci tation</p>
      <div class="bar"><span>70% success</span></div>
      <div class="pill">$ 90 000 invested</div>
      <div class="meta"><span>200 INVESTORS</span><span>23 DAYS LEFT</span></div>
      <span class="invest">INVEST</span>
    </div>
    <div class="col">
      <h3>POPULAR</h3>
      <div class="thumb"><div role="img" aria-label="Businessman celebrating under falling banknotes" style="background:radial-gradient(circle at 50% 55%,#a56b52,#e6e9e0 70%)"></div></div>
      <p>Ut wisi enim ad minim<br>veniam, quis nostrud<br>exerci tation</p>
      <div class="bar"><span>70% success</span></div>
      <div class="pill">$ 90 000 invested</div>
      <div class="meta"><span>200 INVESTORS</span><span>23 DAYS LEFT</span></div>
      <span class="invest">INVEST</span>
    </div>
    <div class="col">
      <h3>MOST INVESTED</h3>
      <div class="thumb"><div role="img" aria-label="Tall stacks of gold coins" style="background:radial-gradient(circle at 50% 55%,#a8793c,#f4efe6 75%)"></div></div>
      <p>Ut wisi enim ad minim<br>veniam, quis nostrud<br>exerci tation</p>
      <div class="bar"><span>70% success</span></div>
      <div class="pill">$ 90 000 invested</div>
      <div class="meta"><span>200 INVESTORS</span><span>23 DAYS LEFT</span></div>
      <span class="invest">INVEST</span>
    </div>
    <div class="col">
      <h3>NEW</h3>
      <div class="thumb"><div role="img" aria-label="Pile of banknote bundles" style="background:radial-gradient(circle at 50% 50%,#8d9a88,#f3f4f2 72%)"></div></div>
      <p>Ut wisi enim ad minim<br>veniam, quis nostrud<br>exerci tation</p>
      <div class="bar"><span>70% success</span></div>
      <div class="pill">$ 90 000 invested</div>
      <div class="meta"><span>200 INVESTORS</span><span>23 DAYS LEFT</span></div>
      <span class="invest">INVEST</span>
    </div>
  </div>

  <div class="abs tab login">LOGIN</div>
  <div class="abs tab signup">SIGN UP</div>
  <div class="abs loginbox">
    <label>Email or Phone</label>
    <div class="field"></div>
    <label>Password</label>
    <div class="field" style="margin-bottom:10px"></div>
    <span class="forgot">Forgot password?</span>
    <span class="logbtn">LOG IN</span>
  </div>

  <div class="abs video">
    <svg class="abs" style="left:102px;top:75px" width="12" height="12" viewBox="0 0 12 12"><circle cx="6" cy="6" r="4.5" fill="none" stroke="#888" stroke-width="2" stroke-dasharray="3 2"/></svg>
    <div class="ctl"></div>
  </div>

  <div class="abs banner">
    <span>View all projects ? More than 1000 projects</span>
    <div class="yes">YES</div>
  </div>

  <div class="abs social" style="left:1003px"></div>
  <div class="abs social" style="left:1038px"></div>
  <div class="abs social" style="left:1073px"></div>

  <div class="abs footer"></div>
  <div class="fcol" style="left:115px"><p>Ut wisi enim ad minim veniam, quis nostrud</p><p>exerci tation ullamcorper suscipit lobortis nisl ut aliquip ex ea commodo consequat.</p><p>Ut wisi enim ad minim veniam, quis nostrud exerci tation ullamcorper suscipit lobortis nisl ut aliquip ex ea commodo consequat.</p></div>
  <div class="fcol" style="left:294px"><p>Ut wisi enim ad minim veniam, quis nostrud</p><p>exerci tation ullamcorper suscipit lobortis nisl ut aliquip ex ea commodo consequat.</p><p>Ut wisi enim ad minim veniam, quis nostrud exerci tation ullamcorper suscipit lobortis nisl ut aliquip ex ea commodo consequat.</p></div>
  <div class="fcol" style="left:461px"><p>Ut wisi enim ad minim veniam, quis nostrud</p><p>exerci tation ullamcorper suscipit lobortis nisl ut aliquip ex ea commodo consequat.</p><p>Ut wisi enim ad minim veniam, quis nostrud exerci tation ullamcorper suscipit lobortis nisl ut aliquip ex ea commodo consequat.</p></div>
  <div class="fcol" style="left:633px"><p>Ut wisi enim ad minim veniam, quis nostrud</p><p>exerci tation ullamcorper suscipit lobortis nisl ut aliquip ex ea commodo consequat.</p><p>Ut wisi enim ad minim veniam, quis nostrud exerci tation ullamcorper suscipit lobortis nisl ut aliquip ex ea commodo consequat.</p></div>
  <div class="fcol" style="left:802px"><p>Ut wisi enim ad minim veniam, quis nostrud</p><p>exerci tation ullamcorper suscipit lobortis nisl ut aliquip ex ea commodo consequat.</p><p>Ut wisi enim ad minim veniam, quis nostrud exerci tation ullamcorper suscipit lobortis nisl ut aliquip ex ea commodo consequat.</p></div>
  <div class="fcol" style="left:974px"><p>Ut wisi enim ad minim veniam, quis nostrud</p><p>exerci tation ullamcorper suscipit lobortis nisl ut aliquip ex ea commodo consequat.</p><p>Ut wisi enim ad minim veniam, quis nostrud exerci tation ullamcorper suscipit lobortis nisl ut aliquip ex ea commodo consequat.</p></div>

  <div class="abs flink" style="left:115px">HELP</div>
  <div class="abs flink" style="left:156px">STYLE</div>
  <div class="abs flink" style="left:198px">GUIDE</div>
  <div class="abs flink" style="left:243px">CONTACT</div>
  <div class="abs flink" style="left:300px">TERMS OF USE</div>
  <div class="abs flink" style="left:375px">PRIVACY POLICY © 2013 HARVEST CELLAR, INC</div>
  <div class="abs flink" style="left:795px">HOME</div>
  <div class="abs flink" style="left:848px">HOW IT WORKS</div>
  <div class="abs flink" style="left:935px">PROJECT REVIEW</div>
  <div class="abs flink" style="left:1027px">VIRTUAL OFFICE</div>
</div>
</body>
</html>
```